Stationery Project with Logo Design

We need stationery & logo design for a new small boutique marketing company based in Perth Western Australia. The company is called Blue Harbor Marketing.

We offer marketing services to small-to-medium business.

We would like to see designs strong & innovative designs and should use red as one of the colours.

The final design should communicate innovation and fun.

Target Market(s)

Small to medium business owners between 20 - 50 years

Industry/Entity Type

Business

Logo Text

```html
<!DOCTYPE html>
<html lang="en">
<head>
<meta charset="utf-8">
<title>Blue Harbor Marketing — Letterhead</title>
<link href="https://fonts.googleapis.com/css2?family=Questrial&display=swap" rel="stylesheet">
<style>
  :root {
    --backdrop: #dcdcdc;
    --paper: #f4f4f4;
    --brand-red: #b0272d;
    --brand-grey: #6b6b6b;
    --ink: #7a7a7a;
    --band-grey: #707070;
  }
  * { box-sizing: border-box; margin: 0; padding: 0; }
  html, body {
    width: 1200px;
    height: 968px;
    overflow: hidden;
    background: var(--backdrop);
    font-family: "Questrial", "Helvetica Neue", Arial, sans-serif;
  }
  .letterhead {
    position: absolute;
    left: 252px;
    top: 34px;
    width: 696px;
    height: 900px;
    background: var(--paper);
    box-shadow: 0 6px 24px rgba(0, 0, 0, 0.12);
  }
  .brand {
    position: absolute;
    left: 48px;
    top: 48px;
    display: flex;
    align-items: center;
    gap: 10px;
  }
  .brand-dot {
    width: 14px;
    height: 14px;
    border-radius: 50%;
    background: var(--brand-red);
  }
  .brand-name {
    color: var(--brand-grey);
    font-size: 24px;
    letter-spacing: 0.5px;
    text-transform: uppercase;
    line-height: 1;
  }
  .contact {
    position: absolute;
    right: 48px;
    top: 132px;
    text-align: right;
    font-size: 9.5px;
    line-height: 1.55;
    color: var(--ink);
  }
  .contact .label { color: var(--brand-red); font-weight: 400; }
  .footer-band {
    position: absolute;
    left: 0;
    right: 0;
    bottom: 0;
    height: 14px;
    display: flex;
    gap: 4px;
  }
  .footer-band .band-red { flex: 0 0 42%; background: var(--brand-red); }
  .footer-band .band-grey { flex: 1; background: var(--band-grey); }
</style>
</head>
<body>
  <main class="letterhead">
    <header class="brand">
      <span class="brand-dot"></span>
      <span class="brand-name">Blue Harbor Marketing</span>
    </header>
    <address class="contact">
      <div>27 Harbour View Dr, Perth, WA 6000</div>
      <div><span class="label">Phone:</span> (08) 9421-0456 · <span class="label">Fax:</span> (08) 9421-0457</div>
      <div><span class="label">Web:</span> www.blueharbormkt.com</div>
    </address>
    <div class="footer-band">
      <span class="band-red"></span>
      <span class="band-grey"></span>
    </div>
  </main>
</body>
</html>
```